Ridgely Forge business card for handing simple contact information and generating service awareness

Utilizing the attached logo(s), generate a professional, but approachable, card conveying a sense of capability and integrity. Please only use one logo of the four attached; the different colors are all acceptable, but preference will be given to a design integrating a teal/turquoise logo,

I do not know where to put in the contact information or details?

Target Market(s)

Agriculture, Farming, Timber, Forestry, Construction, Crane Service

Industry/Entity Type

Contact Information for Business Card

Name, Phone Number, email address

Colors

Designer to choose colors to be used in the design.

Requirements
Nice to have
• It would be great to have either a mountain or one of the attached cranes as a backdrop on the rear of the card. Simple watermarks and/or Debossing is also great

```html
<!DOCTYPE html>
<html lang="en">
<head>
<meta charset="utf-8">
<title>Ridgely Forge – Business Card</title>
<link href="https://fonts.googleapis.com/css2?family=Arimo:wght@400;700&display=swap" rel="stylesheet">
<style>
  :root {
    --teal: #2f6f62;
    --teal-deep: #275f54;
    --paper: #f7f7f5;
    --ink: #222222;
    --muted: #6b6b6b;
    --backdrop: #a3a3a3;
  }
  * { box-sizing: border-box; margin: 0; padding: 0; }
  html, body { width: 1200px; height: 1050px; overflow: hidden; }
  body {
    background: var(--backdrop);
    font-family: "Arimo", Arial, sans-serif;
    position: relative;
  }

  .card {
    position: absolute;
    border-radius: 26px;
  }

  /* Front: portrait contact side */
  .card-front {
    left: 70px; top: 190px;
    width: 380px; height: 665px;
    background: var(--paper);
    border: 4px solid var(--teal);
    display: flex; flex-direction: column; align-items: center;
    padding-top: 78px;
    text-align: center;
  }
  .brand-mark {
    display: flex; align-items: center; gap: 10px;
  }
  .brand-dot {
    width: 30px; height: 30px; border-radius: 50%;
    background: var(--teal);
  }
  .brand-name {
    font-weight: 700; color: var(--teal);
    font-size: 26px; letter-spacing: 0.5px; text-transform: uppercase;
  }
  .person-name {
    margin-top: 54px;
    font-weight: 700; font-size: 30px; color: var(--teal);
  }
  .person-role {
    margin-top: 4px; font-size: 20px; color: var(--muted);
  }
  .icon-row {
    margin-top: 26px;
    display: flex; align-items: center; gap: 8px;
  }
  .icon-row .dash { width: 16px; height: 2px; background: var(--ink); }
  .icon-row svg { width: 26px; height: 26px; display: block; }
  .contact-lines {
    margin-top: 22px;
    font-size: 19px; line-height: 1.3; color: var(--ink);
  }
  .divider {
    margin: 30px 0 28px;
    width: 120px; height: 2px; background: #8a8a8a;
  }
  .address {
    font-size: 19px; line-height: 1.3; color: var(--ink);
  }

  /* Back: landscape brand side */
  .card-back {
    left: 510px; top: 470px;
    width: 630px; height: 360px;
    background: var(--teal);
    border: 4px solid #ffffff;
    display: flex; align-items: center; justify-content: center;
  }
  .card-back .brand-mark { gap: 16px; }
  .card-back .brand-dot {
    width: 48px; height: 48px; background: var(--paper);
  }
  .card-back .brand-name {
    color: var(--paper); font-size: 46px; letter-spacing: 1px;
  }
</style>
</head>
<body>

  <section class="card card-front" aria-label="Card front">
    <div class="brand-mark">
      <span class="brand-dot"></span>
      <span class="brand-name">Ridgely Forge</span>
    </div>

    <h1 class="person-name">Owen Hartley</h1>
    <p class="person-role">President</p>

    <div class="icon-row">
      <span class="dash"></span>
      <svg viewBox="0 0 26 26" aria-label="Phone">
        <circle cx="13" cy="13" r="13" fill="var(--teal)"/>
        <path d="M9 7.5l2.2-.5 1.2 3-1.4 1a7 7 0 0 0 3.5 3.5l1-1.4 3 1.2-.5 2.2c-5.5.4-9.4-3.5-9-9z" fill="#fff"/>
      </svg>
      <svg viewBox="0 0 26 26" aria-label="Email">
        <circle cx="13" cy="13" r="13" fill="var(--teal)"/>
        <rect x="7" y="8.5" width="12" height="9" rx="1" fill="#fff"/>
        <path d="M7.5 9.2L13 13.5l5.5-4.3" stroke="var(--teal)" stroke-width="1.3" fill="none"/>
      </svg>
      <svg viewBox="0 0 26 26" aria-label="Website">
        <circle cx="13" cy="13" r="13" fill="var(--teal)"/>
        <circle cx="13" cy="13" r="6" fill="none" stroke="#fff" stroke-width="1.4"/>
        <ellipse cx="13" cy="13" rx="2.6" ry="6" fill="none" stroke="#fff" stroke-width="1.2"/>
        <line x1="7" y1="13" x2="19" y2="13" stroke="#fff" stroke-width="1.2"/>
      </svg>
      <span class="dash"></span>
    </div>

    <div class="contact-lines">
      <p>(555) 0142-7781</p>
      <p>name@RIDGELYFORGE.com</p>
      <p>www.RIDGELYFORGE.com</p>
    </div>

    <div class="divider"></div>

    <div class="address">
      <p>2190 Larchmont Road</p>
      <p>Cedar Hollow, NY 10000</p>
    </div>
  </section>

  <section class="card card-back" aria-label="Card back">
    <div class="brand-mark">
      <span class="brand-dot"></span>
      <span class="brand-name">Ridgely Forge</span>
    </div>
  </section>

</body>
</html>
```